https://dorvakel.com

We need a cool technology design for our Managed IT Services company. We are located in Coral Springs Florida. We provide all IT services and support for small to medium sized businesses. We would like to see designs that use our blue and white colors from our website.

```html
<!DOCTYPE html>
<html lang="en">
<head>
<meta charset="utf-8">
<title>Dorvakel Business Card</title>
<link href="https://fonts.googleapis.com/css2?family=Source+Sans+3:wght@400;600&display=swap" rel="stylesheet">
<style>
  :root {
    --navy: #002d57;
    --white: #ffffff;
    --paper: #f7f7f7;
    --mist: #dcdcdd;
    --stage: #dddcdd;
  }
  * { box-sizing: border-box; margin: 0; padding: 0; }
  html, body { width: 1200px; height: 1200px; overflow: hidden; }
  body {
    background: var(--stage);
    font-family: "Source Sans 3", "Myriad Pro", sans-serif;
    position: relative;
  }
  .card {
    position: absolute;
    left: 120px;
    width: 960px;
    height: 548px;
    overflow: hidden;
    box-shadow: 0 6px 14px rgba(0,0,0,0.18);
  }
  .card--details { top: 40px; background: linear-gradient(160deg, #fafafa 30%, #d9d9da 100%); }
  .card--brand { top: 612px; background: var(--white); }

  .details__panel { position: absolute; inset: 0; width: 100%; height: 100%; }

  .name-tag__name {
    position: absolute; left: 150px; top: 88px;
    font-size: 50px; line-height: 60px; color: var(--navy); font-weight: 400; letter-spacing: -1px;
  }
  .name-tag__role {
    position: absolute; left: 210px; top: 148px;
    font-size: 17px; line-height: 20px; color: var(--navy);
  }
  .contact {
    position: absolute; left: 60px; color: var(--white);
    display: flex; align-items: center; gap: 48px;
  }
  .contact--address { top: 262px; }
  .contact--phone { top: 366px; }
  .contact__text { font-size: 21px; line-height: 1.35; }
  .contact__text--phone { font-size: 36px; }
  .contact svg { width: 48px; height: 48px; flex: none; }

  .details__mark {
    position: absolute; left: 60px; bottom: 40px;
    color: var(--white); font-size: 30px; font-weight: 600; letter-spacing: 0.5px;
  }
  .services {
    position: absolute; right: 40px; top: 270px;
    list-style: none; text-align: right; color: var(--navy);
  }
  .services li { font-size: 33px; line-height: 1.2; }
  .services li::after {
    content: ""; display: inline-block; width: 22px; height: 6px;
    background: var(--navy); margin-left: 16px; vertical-align: middle;
  }

  .brand__corners { position: absolute; inset: 0; width: 100%; height: 100%; }
  .brand__name {
    position: absolute; left: 0; right: 0; top: 190px;
    display: flex; justify-content: center; align-items: center; gap: 22px;
    color: var(--navy); font-size: 110px; font-weight: 600; letter-spacing: 2px;
  }
  .brand__dot { width: 34px; height: 34px; border-radius: 50%; background: var(--mist); }
  .brand__band {
    position: absolute; left: 0; right: 0; bottom: 0; height: 116px;
    background: var(--navy); color: var(--white);
    display: flex; align-items: center; justify-content: center;
    font-size: 38px;
  }
</style>
</head>
<body>

<section class="card card--details">
  <svg class="details__panel" viewBox="0 0 960 548" preserveAspectRatio="none">
    <polygon points="0,0 610,0 320,548 0,548" fill="#002d57"/>
    <polygon points="0,80 430,80 470,130 430,180 0,180" fill="#f7f7f7"/>
  </svg>
  <h1 class="name-tag__name">Marcus Ellery</h1>
  <p class="name-tag__role">CEO &amp; Founder</p>

  <div class="contact contact--address">
    <svg viewBox="0 0 48 48" aria-hidden="true">
      <path d="M4 12 L16 8 L30 12 L44 8 V38 L30 42 L16 38 L4 42 Z" fill="none" stroke="#fff" stroke-width="3" stroke-linejoin="round"/>
      <path d="M24 14 a7 7 0 0 1 7 7 c0 5 -7 12 -7 12 s-7 -7 -7 -12 a7 7 0 0 1 7 -7 z" fill="#fff"/>
      <circle cx="24" cy="21" r="2.6" fill="#002d57"/>
    </svg>
    <p class="contact__text">2750 Harbor Palm Way #180<br>Palm Crest, Florida 33088</p>
  </div>

  <div class="contact contact--phone">
    <svg viewBox="0 0 48 48" aria-hidden="true">
      <path d="M12 4 l8 9 -5 6 c3 6 8 11 14 14 l6 -5 9 8 -6 8 C20 44 4 28 4 10 Z" fill="#fff"/>
    </svg>
    <p class="contact__text contact__text--phone">(555) 204-7719</p>
  </div>

  <p class="details__mark">DORVAKEL</p>

  <ul class="services">
    <li>Managed IT</li>
    <li>Security Services</li>
    <li>Cloud IT</li>
    <li>Industry Solutions</li>
  </ul>
</section>

<section class="card card--brand">
  <svg class="brand__corners" viewBox="0 0 960 548" preserveAspectRatio="none">
    <polygon points="0,0 80,50 0,140" fill="#002d57"/>
    <polygon points="960,0 960,140 890,70" fill="#002d57"/>
  </svg>
  <div class="brand__name"><span class="brand__dot"></span>DORVAKEL</div>
  <div class="brand__band">www.dorvakel.com</div>
</section>

</body>
</html>
```